Collectibles expert needs a new business card design.

My current business card makes me look to high end. It may even make me look arrogant or too stuffy. I do work with high end clients and their items but most of my business is with average people with average items. My business name is Walter Brumby's Old Mill Digging Co. The idea was that I mine the streets helping people discover the treasures buried in their homes. That could be art, jewelry, coins, etc. The name and an older logo I used does not make immediate sense to most people. I tried to go with just my picture and name and that is the current card I am changing. I help people who need to downsize. Whether they are getting rid of one item, a collection or a house full of items I help them discover what they have, what it is worth and what are the best ways we can get the most for them. This may be a combination of estate sale (which I dont do) auction or sell directly to a dealer or collector. Usually it is a combination of these. My main goal is to help make sure they dont accidently sell a Vandermeer painting in a garage sale. I am uploading a copy of my old card and the old logo I used to use but the winning card design will need to be much different than these. You can learn a little more about me at www.walterkbrumby.example, www.oldmilldigng.example and www.facebook.com/omdco. I hope someone can look at what I do and come up with a very unique design that will be equally effective if my client is high income or if my client is low to mid income. I do not care if it is a one or two sided card as long as it conveys my contact information and a good representation of what I do.

Target Market(s)

People who are getting rid of items. These can be elderly couples or individuals that are moving to an active living community and will have less space so they need to sell items. This can also include the children of elder parents that dont want their stuff and want to find solutions to help them get rid of their items.

Contact Information for Business Card

The card should have my business name Walter Brumby's Old Mill Digging Co., phone number 555-312-70981, email walter@oldmilldigging.example and website www.oldmilldigging.example. Would also like to include Buyer, Broker, Consultant and Appraiser. We can put Walter K. Brumby, ISA on the opposite side of the company name since it includes my name as well.

Font styles to use
Sans Serif

Colors

Designer to choose colors to be used in the design.

Requirements
Must have
• My project must have a professional look. It must not alienate low income clients and should still be appealing to high value clients.

```html
<!DOCTYPE html>
<html lang="en">
<head>
<meta charset="utf-8">
<title>Walter Brumby's Old Mill Digging Co. — Business Card</title>
<link rel="stylesheet" href="https://fonts.googleapis.com/css2?family=Oswald:wght@500;600&family=Lato:wght@400&display=swap">
<style>
  :root {
    --backdrop: #1c1c1d;
    --card: #121213;
    --gold: #c08a2c;
    --gold-soft: #b9852d;
    --white: #f1f1f1;
    --rule: #5a5a5a;
  }
  * { box-sizing: border-box; margin: 0; padding: 0; }
  html, body {
    width: 1200px;
    height: 900px;
    overflow: hidden;
    background: var(--backdrop);
  }
  .sheet {
    position: relative;
    width: 1200px;
    height: 900px;
    display: flex;
    flex-direction: column;
    align-items: center;
    justify-content: center;
    gap: 50px;
  }
  .card {
    width: 560px;
    height: 320px;
    background: var(--card);
    border-radius: 24px;
    box-shadow: 0 18px 40px rgba(0, 0, 0, 0.55);
    display: flex;
    flex-direction: column;
    align-items: center;
    justify-content: center;
    text-align: center;
  }
  /* Front side */
  .brand {
    display: flex;
    flex-direction: column;
    align-items: center;
    gap: 22px;
  }
  .brand-mark {
    width: 64px;
    height: 64px;
    background: var(--gold);
  }
  .brand-name {
    font-family: "Oswald", sans-serif;
    font-weight: 600;
    font-size: 30px;
    letter-spacing: 0.5px;
    text-transform: uppercase;
    color: var(--gold);
    line-height: 1.15;
    max-width: 440px;
  }
  /* Back side */
  .person-name {
    font-family: "Oswald", sans-serif;
    font-weight: 500;
    font-size: 24px;
    letter-spacing: 0.5px;
    text-transform: uppercase;
    color: var(--gold);
  }
  .role {
    font-family: "Lato", sans-serif;
    font-size: 17px;
    color: var(--white);
    margin-top: 2px;
  }
  .divider {
    width: 170px;
    height: 1px;
    background: var(--rule);
    margin: 16px 0 14px;
  }
  .divider.wide { width: 260px; margin-top: 14px; }
  .contact {
    font-family: "Lato", sans-serif;
    font-size: 17px;
    color: var(--white);
    line-height: 1.45;
  }
  .contact .label { color: var(--gold); }
  .website {
    font-family: "Lato", sans-serif;
    font-size: 17px;
    color: var(--gold-soft);
    line-height: 1.45;
  }
</style>
</head>
<body>
  <main class="sheet">
    <section class="card card-front">
      <div class="brand">
        <div class="brand-mark"></div>
        <p class="brand-name">Walter Brumby's Old Mill Digging Co.</p>
      </div>
    </section>

    <section class="card card-back">
      <h1 class="person-name">Walter K. Brumby, ISA</h1>
      <p class="role">Buyer, Broker, Consultant and Appraiser</p>
      <div class="divider"></div>
      <p class="contact"><span class="label">P:</span> 555-312-70981</p>
      <p class="contact"><span class="label">E:</span> walter@oldmilldigging.example</p>
      <p class="website">www.oldmilldigging.example</p>
    </section>
  </main>
</body>
</html>
```